Promotional Post crad

SEE SAMPLE POST CARD <br/><br/>Everything in our lab is manufactured inhouse. No outsourcing !<br/><br/>FULL SERVICE DIGITAL DENTAL LABORATORY<br/><br/>We restore all implants <br/><br/>Implant packages starting from $499<br/><br/>Full contour zirconia crown $99<br/><br/>Build up zirconia crown $179<br/><br/>Implant package promotion starting at 499<br/><br/>Try to make the same design on the back of the card with different parts adding up to the final product

Target Market(s)

Dentists

```html
<!DOCTYPE html>
<html lang="en">
<head>
<meta charset="utf-8">
<title>Dental Lab Postcard</title>
<link href="https://fonts.googleapis.com/css2?family=Bebas+Neue&family=Montserrat:wght@400;500;600;700&display=swap" rel="stylesheet">
<style>
  :root {
    --bg: #7b7776;
    --green: #0b8a3e;
    --green-light: #22b055;
    --blue: #2b86cf;
    --blue-dark: #1f6fb6;
    --white: #ffffff;
    --ink: #1c1c1c;
    --grey: #b9b9b9;
    --line: #e6e6e6;
  }
  html, body { margin: 0; padding: 0; overflow: hidden; }
  body {
    width: 1200px; height: 1200px; background: var(--bg);
    position: relative; font-family: "Montserrat", sans-serif;
  }
  .card {
    position: absolute; left: 200px; width: 1000px; height: 666px;
    transform: scale(0.8); transform-origin: 0 0;
    background: var(--white); overflow: hidden;
  }
  .card--front { top: 46px; }
  .card--back { top: 622px; }
  .card svg.shapes { position: absolute; inset: 0; width: 1000px; height: 666px; }
  .abs { position: absolute; }
  .brand { display: flex; align-items: center; gap: 10px; }
  .brand__dot { width: 22px; height: 22px; border-radius: 50%; background: var(--green); }
  .brand__name { font-weight: 700; color: var(--green); font-size: 30px; }
  .front__brand { left: 745px; top: 100px; }
  .front__lead {
    margin: 0; left: 560px; top: 226px; width: 401px; text-align: right;
    font-size: 30px; line-height: 39px; color: var(--ink); letter-spacing: 0.5px;
  }
  .front__headline {
    left: 560px; top: 308px; width: 401px; text-align: right;
    font-family: "Bebas Neue", sans-serif; font-size: 66px; color: var(--blue-dark); line-height: 1;
  }
  .phone {
    left: 580px; top: 428px; width: 420px; height: 76px;
    background: var(--green); border-radius: 38px 0 0 38px;
    display: flex; align-items: center;
  }
  .phone__icon { margin-left: 8px; width: 62px; height: 62px; }
  .phone__number {
    font-family: "Bebas Neue", sans-serif; font-size: 70px; color: var(--white);
    margin-left: 14px; line-height: 1; padding-top: 6px;
  }
  .front__web { left: 678px; top: 590px; font-size: 21px; color: var(--white); letter-spacing: 1px; }

  .back__title {
    left: 42px; top: 38px; font-family: "Bebas Neue", sans-serif;
    font-size: 50px; line-height: 48px; color: var(--white);
  }
  .back__sub { left: 43px; top: 132px; font-size: 28px; color: var(--white); letter-spacing: 0.5px; }
  .back__rule { left: 43px; top: 176px; width: 104px; height: 4px; background: var(--white); }
  .offers { left: 43px; top: 202px; display: flex; gap: 16px; }
  .offer {
    width: 98px; height: 80px; box-sizing: border-box;
    background: linear-gradient(#3a95dc, var(--blue-dark));
    border: 2px solid var(--green-light); border-radius: 6px;
    color: var(--white); text-align: center; display: flex; flex-direction: column;
    justify-content: space-between; padding: 6px 3px 4px;
  }
  .offer__label { font-size: 11px; line-height: 13px; padding-bottom: 3px; border-bottom: 1px solid rgba(255,255,255,.5); }
  .offer__label--small { font-size: 9px; line-height: 11px; }
  .offer__price { font-size: 21px; font-weight: 700; line-height: 24px; }
  .back__brand { left: 628px; top: 105px; }
  .back__brand .brand__dot { width: 14px; height: 14px; }
  .back__brand .brand__name { font-size: 16px; }
  .address { left: 622px; top: 150px; font-size: 14px; line-height: 17px; color: var(--ink); display: flex; gap: 6px; }
  .stamp { left: 857px; top: 83px; width: 88px; height: 100px; background: #f2f2f2; }
  .address-line { left: 588px; width: 357px; height: 1px; background: var(--line); }
</style>
</head>
<body>

<section class="card card--front">
  <svg class="shapes" viewBox="0 0 1000 666">
    <defs>
      <linearGradient id="greenBand" x1="0" x2="1">
        <stop offset="0" stop-color="#22b055"/><stop offset="1" stop-color="#0b7f38"/>
      </linearGradient>
      <linearGradient id="photoTone" x1="0" y1="0" x2="1" y2="1">
        <stop offset="0" stop-color="#dfe6e6"/><stop offset="0.6" stop-color="#e8c8ae"/><stop offset="1" stop-color="#3f8fb4"/>
      </linearGradient>
    </defs>
    <path d="M0 590 C150 690 420 680 560 600 C760 540 900 520 1000 575 V666 H0 Z" fill="url(#greenBand)"/>
    <path d="M0 590 C160 680 420 670 560 595 C760 530 900 515 1000 568 V582 C900 530 760 548 560 608 C420 688 150 700 0 605 Z" fill="var(--grey)"/>
    <path d="M0 0 H695 C560 130 530 420 420 570 C310 690 90 660 0 560 Z" fill="var(--blue)"/>
    <path d="M0 0 H682 C545 130 515 410 405 555 C300 665 100 640 0 545 Z" fill="var(--white)"/>
    <path d="M0 0 H672 C535 130 503 400 395 545 C290 650 110 620 0 525 Z" fill="url(#photoTone)" role="img" aria-label="Photo of a dentist examining a young woman's teeth"/>
    <path d="M695 0 H708 C575 130 545 430 435 580 C325 700 90 675 0 575 V560 C90 660 310 690 420 570 C530 420 560 130 695 0 Z" fill="var(--grey)"/>
  </svg>
  <div class="abs brand front__brand"><span class="brand__dot"></span><span class="brand__name">Meridental</span></div>
  <p class="abs front__lead">Everything in our lab is manufactured inhouse.</p>
  <div class="abs front__headline">NO OUTSOURCING !</div>
  <div class="abs phone">
    <svg class="phone__icon" viewBox="0 0 62 62">
      <circle cx="31" cy="31" r="28" fill="none" stroke="#fff" stroke-width="4"/>
      <path d="M22 17 L27 16 L30 24 L26 27 C28 32 31 35 35 37 L38 33 L46 36 L45 41 C43 45 38 46 33 43 C26 39 21 34 18 27 C16 22 18 18 22 17 Z" fill="#fff"/>
    </svg>
    <span class="phone__number">012-345-6789</span>
  </div>
  <div class="abs front__web">www.companyname.com</div>
</section>

<section class="card card--back">
  <svg class="shapes" viewBox="0 0 1000 666">
    <defs>
      <linearGradient id="familyTone" x1="0" y1="0" x2="1" y2="1">
        <stop offset="0" stop-color="#e7c4a6"/><stop offset="0.5" stop-color="#c9d6e8"/><stop offset="1" stop-color="#e9a6b8"/>
      </linearGradient>
    </defs>
    <path d="M700 0 H716 C590 110 560 330 505 470 C440 640 180 670 0 600 V585 C180 655 430 625 490 465 C545 325 575 110 700 0 Z" fill="var(--grey)"/>
    <path d="M0 0 H700 C575 110 545 325 490 465 C430 625 180 655 0 585 Z" fill="var(--blue)"/>
    <path d="M0 0 H695 C565 110 535 320 478 455 C420 600 190 630 0 560 Z" fill="var(--green)"/>
    <path d="M0 335 C60 310 420 300 462 330 C450 380 445 420 432 450 C380 580 190 610 0 545 Z" fill="url(#familyTone)" role="img" aria-label="Photo of a smiling multi-generation family"/>
  </svg>
  <div class="abs back__title">FULL SERVICE<br>DIGITAL DENTAL LABORATORY</div>
  <div class="abs back__sub">We restore all implants</div>
  <div class="abs back__rule"></div>
  <div class="abs offers">
    <div class="offer"><span class="offer__label">Implant packages starting from</span><span class="offer__price">$499</span></div>
    <div class="offer"><span class="offer__label">Full contour zirconia crown</span><span class="offer__price">$99</span></div>
    <div class="offer"><span class="offer__label">Build up zirconia crown</span><span class="offer__price">$179</span></div>
    <div class="offer"><span class="offer__label offer__label--small">Implant package promotion starting at</span><span class="offer__price">$499</span></div>
  </div>
  <div class="abs brand back__brand"><span class="brand__dot"></span><span class="brand__name">Meridental</span></div>
  <div class="abs address">
    <svg width="14" height="16" viewBox="0 0 14 16"><path d="M7 1 C3.5 1 1.5 3.5 1.5 6 C1.5 9.5 7 15 7 15 C7 15 12.5 9.5 12.5 6 C12.5 3.5 10.5 1 7 1 Z" fill="none" stroke="#2b86cf" stroke-width="1.6"/><circle cx="7" cy="6" r="2" fill="#2b86cf"/></svg>
    <span>lorem ipsum,123 any<br>street, city name,</span>
  </div>
  <div class="abs stamp"></div>
  <div class="abs address-line" style="top:270px"></div>
  <div class="abs address-line" style="top:364px"></div>
  <div class="abs address-line" style="top:458px"></div>
  <div class="abs address-line" style="top:552px"></div>
</section>

</body>
</html>
```